Young girl personal stationary

I need a design for stationary for my daughter. She is two. Other than a flap card and envelope, I will also need a gift tag. She is very lively and active. She loves ducks. Her name is Tavi, which means "a rare pearl". Tavi also LOVES perfume bottles.

Perfume

```html
<!DOCTYPE html>
<html lang="en">
<head>
<meta charset="utf-8">
<title>Tavi Stationery Set</title>
<link rel="stylesheet" href="https://fonts.googleapis.com/css2?family=Open+Sans:wght@400;600&display=swap">
<style>
  :root {
    --backdrop: #f3ece6;
    --pink: #e8188c;
    --pink-soft: #f58cc4;
    --glow: #fff4fa;
    --name-ink: #c0156f;
    --flap: #b24c8c;
    --flap-inner: #a94584;
    --rule: #9a8c98;
    --label: #8a7f88;
  }
  * { box-sizing: border-box; margin: 0; padding: 0; }
  html, body {
    width: 1200px;
    height: 803px;
    overflow: hidden;
    background: var(--backdrop);
  }
  .set {
    position: relative;
    width: 1200px;
    height: 803px;
  }
  .paper-glow {
    background: radial-gradient(ellipse at 50% 48%, var(--glow) 0%, var(--pink-soft) 48%, var(--pink) 100%);
  }
  .name {
    font-family: "Open Sans", "Arial", sans-serif;
    font-weight: 600;
    color: var(--name-ink);
    line-height: 1;
  }

  /* Letter sheet */
  .letter-sheet {
    position: absolute;
    left: 120px;
    top: 300px;
    width: 280px;
    height: 390px;
    box-shadow: 0 6px 14px rgba(0,0,0,.18);
  }
  .letter-sheet .ruling {
    position: absolute;
    inset: 24px 22px 24px 22px;
    background: repeating-linear-gradient(to bottom, transparent 0 20px, var(--rule) 20px 21px);
    opacity: .7;
  }
  .letter-sheet .name {
    position: absolute;
    left: 0; right: 0;
    top: 160px;
    text-align: center;
    font-size: 50px;
  }

  /* Envelope */
  .envelope {
    position: absolute;
    left: 480px;
    top: 145px;
    width: 340px;
    height: 300px;
  }
  .envelope .flap {
    position: absolute;
    left: 10px; right: 10px; top: 0;
    height: 64px;
    background: var(--flap);
    clip-path: polygon(0 100%, 4% 0, 96% 0, 100% 100%);
  }
  .envelope .body {
    position: absolute;
    left: 0; right: 0; top: 56px; bottom: 0;
    box-shadow: 0 6px 14px rgba(0,0,0,.18);
  }
  .envelope .pocket {
    position: absolute;
    left: 30px; right: 30px; top: 0;
    height: 48px;
    background: var(--flap-inner);
  }
  .envelope .name {
    position: absolute;
    left: 28px;
    top: 100px;
    font-size: 40px;
  }

  /* Gift tags */
  .gift-tag {
    position: absolute;
    width: 210px;
    height: 120px;
    filter: drop-shadow(0 4px 8px rgba(0,0,0,.2));
  }
  .gift-tag .shape {
    position: absolute;
    inset: 0;
    clip-path: polygon(16% 0, 100% 0, 100% 100%, 16% 100%, 0 72%, 0 28%);
  }
  .gift-tag .hole {
    position: absolute;
    left: 12px;
    top: 50px;
    width: 18px;
    height: 18px;
    border-radius: 50%;
    background: var(--backdrop);
  }
  .gift-tag .field {
    position: absolute;
    left: 44px;
    width: 90px;
    border-bottom: 1px solid var(--rule);
    font-family: "Open Sans", "Arial", sans-serif;
    font-size: 9px;
    color: var(--label);
    padding-bottom: 2px;
  }
  .gift-tag .field.to { top: 34px; }
  .gift-tag .field.from { top: 66px; }
  .gift-tag .name {
    position: absolute;
    right: 16px;
    top: 48px;
    font-size: 22px;
  }
  .tag-one { left: 880px; top: 380px; }
  .tag-two { left: 880px; top: 510px; }
  .tag-three { left: 880px; top: 640px; }
</style>
</head>
<body>
  <main class="set">
    <section class="letter-sheet paper-glow" aria-label="Letter sheet">
      <div class="ruling"></div>
      <div class="name">Tavi</div>
    </section>

    <section class="envelope" aria-label="Envelope">
      <div class="flap"></div>
      <div class="body paper-glow">
        <div class="pocket"></div>
        <div class="name">Tavi</div>
      </div>
    </section>

    <section class="gift-tag tag-one" aria-label="Gift tag">
      <div class="shape paper-glow"></div>
      <div class="hole"></div>
      <div class="field to">To:</div>
      <div class="field from">From:</div>
      <div class="name">Tavi</div>
    </section>

    <section class="gift-tag tag-two" aria-label="Gift tag">
      <div class="shape paper-glow"></div>
      <div class="hole"></div>
      <div class="field to">To:</div>
      <div class="field from">From:</div>
      <div class="name">Tavi</div>
    </section>

    <section class="gift-tag tag-three" aria-label="Gift tag">
      <div class="shape paper-glow"></div>
      <div class="hole"></div>
      <div class="field to">To:</div>
      <div class="field from">From:</div>
      <div class="name">Tavi</div>
    </section>
  </main>
</body>
</html>
```